Chic streamline modern edgy! Dannokecurls.com

I need a website built for my personal business. I am a hair stylist and I would like a crisp website that works well, is sleek, easy to use, and allows my clients to navigate through Services and pay deposits for services listed.

My logo is somewhat of a full moon, so my theme is nocturnal.

My information can be found at glamnook.com/dannokecurls

Target Market(s)

Women ages 25-55 who are looking for luxury hair extension services

Industry/Entity Type

Hair And Beauty

Number of Pages Required

1 page

Colors
474747
919191
d3d3d3
000000

Requirements
Must have
• Location map, coinvex link embedded for deposits, contact box, bio, faq/policies, menu of services, hours of availability by appointment only .
Nice to have
• An interactive calander where I could post dates that I am available, preferred providers for other beauty services where i could list other websites for make up and other beauty related referrals. a bridal tab would be nice to offer information about bridal services and policies.

```html
<!DOCTYPE html>
<html lang="en">
<head>
<meta charset="utf-8">
<title>Dannoke Curls — Hair Studio</title>
<link href="https://fonts.googleapis.com/css2?family=Lato:ital,wght@0,300;0,400;0,700;1,400&family=Great+Vibes&display=swap" rel="stylesheet">
<style>
:root{
  --black:#000;
  --night:#0c0c0c;
  --header:#1d1d1d;
  --panel:#2a2b2f;
  --card:#1f2023;
  --card-line:#4a4b50;
  --ink:#474747;
  --mid:#919191;
  --soft:#d3d3d3;
  --white:#fff;
  --call:#4b4b4b;
  --pay:#f5b51f;
}
*{box-sizing:border-box;margin:0;padding:0}
html,body{width:1200px;height:3409px;overflow:hidden}
body{background:var(--night);font-family:'Lato',sans-serif;color:var(--soft);position:relative}
.abs{position:absolute}
section,header,footer{position:absolute;left:0;width:1200px}

/* header */
.site-header{top:0;height:127px;background:var(--header);z-index:2}
.brand-mark{left:141px;top:24px;width:36px;height:36px;border-radius:50%;background:var(--ink)}
.brand{left:188px;top:24px;font-size:30px;line-height:36px;font-weight:400;color:var(--white);white-space:nowrap}
.info{font-size:12px;line-height:16px;color:var(--soft);white-space:nowrap}
.info svg{position:absolute;left:-30px;top:3px}
.addr{left:500px;top:28px}
.hours{left:766px;top:28px}
.social{display:flex;gap:6px}
.social span{width:20px;height:20px;border-radius:50%;border:1.5px solid var(--soft)}
.top-social{left:1012px;top:34px}
.nav{left:141px;top:93px;width:648px;height:57px;background:var(--white);display:flex;align-items:center;padding-left:20px}
.nav a{color:#222;text-decoration:none;font-size:13px;padding:0 28px;letter-spacing:.3px;white-space:nowrap}
.nav a.active{font-weight:700}
.call{left:789px;top:93px;width:270px;height:57px;background:var(--call);color:var(--white);font-size:19px;display:flex;align-items:center;gap:10px;padding-left:20px;white-space:nowrap}

/* hero */
.hero{top:127px;height:478px;background:#141414}
.hero-photo{left:130px;top:0;width:1006px;height:478px;background:linear-gradient(90deg,#3a1518 0%,#5a1f24 22%,#2a1a1a 45%,#1b1b1b 70%,#141414 100%)}
.hero-arrow{width:40px;height:40px;border-radius:50%;background:#3a3a3a;display:flex;align-items:center;justify-content:center}
.kicker{left:655px;top:160px;font-family:'Great Vibes',cursive;font-size:34px;color:var(--mid);white-space:nowrap}
.headline{left:655px;top:212px;font-family:'Great Vibes',cursive;font-size:44px;color:var(--white);white-space:nowrap}
.btn{background:var(--soft);color:#111;font-size:14px;display:flex;align-items:center;justify-content:center;white-space:nowrap}
.hero-btn{left:657px;top:287px;width:164px;height:32px}

/* section titles */
.title{width:1200px;text-align:center;font-size:25px;font-weight:400;color:var(--white)}
.title::after{content:"";display:block;width:30px;height:2px;background:var(--white);margin:12px auto 0}

/* services */
.services{top:605px;height:531px;background:var(--panel)}
.service{width:240px;text-align:center;transform:translateX(-50%)}
.service svg{display:block;margin:0 auto 14px}
.service h3{font-size:13px;font-weight:400;color:var(--soft);margin-bottom:16px}
.service p{font-size:10px;line-height:15px;color:var(--mid)}

/* gallery */
.gallery{top:1136px;height:419px;background:var(--night)}
.thumb{top:128px;width:280px;height:225px;border:2px solid var(--soft)}
.side-arrow{top:219px;width:44px;height:44px;border:2px solid var(--soft);border-radius:50%;display:flex;align-items:center;justify-content:center}

/* prices */
.prices{top:1555px;height:570px;background:var(--panel)}
.tab{top:141px;height:30px;font-size:12px;letter-spacing:.4px;display:flex;align-items:center;justify-content:center;color:var(--soft)}
.tab.active{background:var(--black);color:var(--white)}
.price-card{width:440px;height:120px;background:var(--card);border:2px solid var(--card-line);padding:16px}
.price-card .row{display:flex;align-items:center;font-size:17px;color:var(--white)}
.price-card .row .name{flex:1}
.price-card .cost{font-size:14px;margin-right:10px}
.price-card .dur{background:#3c3c3c;font-size:12px;padding:3px 10px}
.price-card p{font-size:10.5px;line-height:15px;color:var(--mid);margin-top:10px}
.book{left:525px;top:491px;width:150px;height:30px;font-size:13px}

/* testimonials */
.reviews{top:2125px;height:557px;background:var(--night)}
.face{border-radius:50%;border:6px solid var(--soft);transform:translate(-50%,-50%)}
.face.small{width:136px;height:136px;background:radial-gradient(circle at 50% 40%,#b8896e,#5c3b2d)}
.face.big{width:186px;height:186px;border-width:8px;background:radial-gradient(circle at 50% 40%,#d6ad8c,#7a4e34)}
.quote{top:384px;width:1200px;text-align:center;font-style:italic;font-size:19px;line-height:32px;color:var(--white)}
.cite{top:462px;width:1200px;text-align:center;font-size:16px;color:var(--white)}
.cite span{color:var(--mid)}
.dots{top:500px;left:580px;display:flex;gap:6px}
.dots i{width:6px;height:6px;border-radius:50%;background:var(--ink)}
.dots i:first-child{background:var(--white)}

/* map */
.map{top:2682px;height:398px;background:linear-gradient(180deg,#ebe6dc,#e2ddd2)}

/* footer */
.site-footer{top:3080px;height:329px;background:var(--black)}
.foot-mark{left:315px;top:74px;width:40px;height:40px;border-radius:50%;background:#2a2a2a}
.foot-brand{left:180px;top:132px;width:310px;text-align:center;font-size:34px;color:#8a8a8a;white-space:nowrap}
.portrait{left:477px;top:34px;width:241px;height:171px;border:3px solid var(--soft);background:linear-gradient(135deg,#dcdcdc,#6e6e6e)}
.contact{left:818px;top:66px;font-size:12px;line-height:16px;color:var(--mid);white-space:nowrap}
.contact h4{font-size:17px;font-weight:400;color:var(--white);margin-bottom:10px}
.contact .phone{font-size:20px;color:var(--white);margin:8px 0}
.rule{left:130px;top:250px;width:940px;height:1px;background:#262626}
.copy{left:141px;top:279px;font-size:13px;color:var(--mid)}
.pay{left:811px;top:270px;width:155px;height:32px;background:var(--pay);color:#1a1a1a;font-size:14px;font-weight:700;display:flex;align-items:center;justify-content:center}
.foot-social{left:1002px;top:272px}
.foot-social span{width:28px;height:28px;border-color:var(--white)}
</style>
</head>
<body>

<section class="hero">
  <div class="abs hero-photo" role="img" aria-label="Portrait of a model with long curled red hair against a dark salon backdrop"></div>
  <div class="abs hero-arrow" style="left:72px;top:214px"><svg width="12" height="14" viewBox="0 0 12 14"><path d="M9 1 3 7l6 6" fill="none" stroke="#fff" stroke-width="2"/></svg></div>
  <div class="abs hero-arrow" style="left:1088px;top:214px"><svg width="12" height="14" viewBox="0 0 12 14"><path d="m3 1 6 6-6 6" fill="none" stroke="#fff" stroke-width="2"/></svg></div>
  <div class="abs kicker">we do everything</div>
  <div class="abs headline">Your Hair may Require</div>
  <div class="abs btn hero-btn">Contact Us Today</div>
</section>

<header class="site-header">
  <div class="abs brand-mark"></div>
  <div class="abs brand">DANNOKE CURLS</div>
  <div class="abs info addr">
    <svg width="16" height="22" viewBox="0 0 16 22"><path d="M8 1a7 7 0 0 0-7 7c0 5 7 13 7 13s7-8 7-13a7 7 0 0 0-7-7z" fill="#d3d3d3"/><circle cx="8" cy="8" r="2.6" fill="#1d1d1d"/></svg>
    Lumen Salon Suite<br>4120 Crescent Road, 9 Dallas, TX
  </div>
  <div class="abs info hours">
    <svg width="20" height="20" viewBox="0 0 20 20"><circle cx="10" cy="10" r="8.5" fill="none" stroke="#d3d3d3" stroke-width="1.6"/><path d="M10 5v5h4" fill="none" stroke="#d3d3d3" stroke-width="1.6"/></svg>
    Tuesday - Saturday 9.00 am - 7.00 pm<br>Sunday &amp; Monday Closed
  </div>
  <div class="abs social top-social"><span></span><span></span></div>
  <nav class="abs nav">
    <a class="active" href="#">HOME</a><a href="#">ABOUT US</a><a href="#">SERVICES</a><a href="#">GALLERY</a><a href="#">CONTACT US</a>
  </nav>
  <div class="abs call">
    <svg width="20" height="20" viewBox="0 0 20 20"><path d="M4 2h4l2 5-2.5 1.5a11 11 0 0 0 4 4L13 10l5 2v4a2 2 0 0 1-2 2A15 15 0 0 1 2 4a2 2 0 0 1 2-2z" fill="#fff"/></svg>
    Call Us : 214-555-0172
  </div>
</header>

<section class="services">
  <h2 class="abs title" style="top:30px">Our Services</h2>

  <div class="abs service" style="left:239px;top:132px">
    <svg width="56" height="44" viewBox="0 0 56 44" fill="none" stroke="#d3d3d3" stroke-width="2"><rect x="6" y="14" width="10" height="26"/><rect x="20" y="6" width="8" height="34"/><rect x="32" y="22" width="6" height="18"/><circle cx="46" cy="34" r="6"/></svg>
    <h3>Professional Makeup</h3>
    <p>Makeup Can Have A Magical Effect<br>When Performed By Real Masters</p>
  </div>
  <div class="abs service" style="left:477px;top:132px">
    <svg width="44" height="44" viewBox="0 0 44 44" fill="none" stroke="#d3d3d3" stroke-width="2"><rect x="10" y="4" width="24" height="36" rx="10"/><rect x="16" y="12" width="12" height="8" fill="#d3d3d3"/></svg>
    <h3>Painless Depilation</h3>
    <p>Beauty Sometimes Requires Pain, But<br>Depilation With Us Can Be Pain-free</p>
  </div>
  <div class="abs service" style="left:718px;top:132px">
    <svg width="44" height="44" viewBox="0 0 44 44" fill="none" stroke="#d3d3d3" stroke-width="2"><circle cx="11" cy="33" r="6"/><circle cx="33" cy="33" r="6"/><path d="M15 29 36 6M29 29 8 6"/></svg>
    <h3>Haircut and Styling</h3>
    <p>It Is Not Just A Job, It Is Art And<br>Pleasure To Work With Woman's Hair</p>
  </div>
  <div class="abs service" style="left:961px;top:132px">
    <svg width="56" height="44" viewBox="0 0 56 44" fill="none" stroke="#d3d3d3" stroke-width="2"><path d="M4 24c12-14 36-14 48 0-12 12-36 12-48 0z"/><circle cx="28" cy="24" r="7" fill="#d3d3d3"/><path d="M8 14 4 8M18 8l-2-6M28 6V0M38 8l2-6M48 14l4-6"/></svg>
    <h3>Eyelash Extensions</h3>
    <p>Nothing Can Grant A Woman Such<br>Charm As Long Curved Eyelashes</p>
  </div>

  <div class="abs service" style="left:239px;top:320px">
    <svg width="48" height="44" viewBox="0 0 48 44" fill="none" stroke="#d3d3d3" stroke-width="2"><path d="M6 40c0-14 6-30 22-34 8-2 14 4 14 10-6 0-10 4-10 10v18z"/></svg>
    <h3>Professional Makeup</h3>
    <p>It Is Not Always Yourself Who Knows<br>Best What Would Fit You Perfectly</p>
  </div>
  <div class="abs service" style="left:477px;top:320px">
    <svg width="44" height="44" viewBox="0 0 44 44" fill="none" stroke="#d3d3d3" stroke-width="2"><circle cx="22" cy="18" r="13"/><path d="M12 30 8 42h28l-4-12M16 16h12M16 22h12"/></svg>
    <h3>Spa Procedures</h3>
    <p>Relaxation And Enjoyment Make You<br>A Different And Happier Person</p>
  </div>
  <div class="abs service" style="left:718px;top:320px">
    <svg width="44" height="44" viewBox="0 0 44 44" fill="none" stroke="#d3d3d3" stroke-width="2"><path d="M10 40 30 20M26 8l10 10-6 6-10-10z"/><path d="M34 4l6 6"/></svg>
    <h3>Regenerating Treatments</h3>
    <p>Absolutely New Technology, Absolutely<br>Exclusive Service For Our VIPs</p>
  </div>
  <div class="abs service" style="left:961px;top:320px">
    <svg width="44" height="44" viewBox="0 0 44 44" fill="none" stroke="#d3d3d3" stroke-width="2"><rect x="10" y="18" width="14" height="22" rx="2"/><path d="M13 18v-6h8v6M30 40V10M27 10h6"/></svg>
    <h3>Manicure &amp; Pedicure</h3>
    <p>Hands And Feet Work For You A Lot,<br>Sometimes They Need Vacation, Too</p>
  </div>
</section>

<section class="gallery">
  <h2 class="abs title" style="top:42px">View Gallery</h2>
  <div class="abs side-arrow" style="left:58px"><svg width="12" height="16" viewBox="0 0 12 16"><path d="M9 2 3 8l6 6" fill="none" stroke="#fff" stroke-width="2.5"/></svg></div>
  <div class="abs side-arrow" style="left:1098px"><svg width="12" height="16" viewBox="0 0 12 16"><path d="m3 2 6 6-6 6" fill="none" stroke="#fff" stroke-width="2.5"/></svg></div>
  <div class="abs thumb" style="left:143px;background:linear-gradient(135deg,#4a3328,#8b6a55 50%,#2e2520)" role="img" aria-label="Collage of sleek bob haircuts"></div>
  <div class="abs thumb" style="left:457px;background:linear-gradient(135deg,#2d4a6a,#1e1e24 50%,#5a6f80)" role="img" aria-label="Collage of long straight extension styles"></div>
  <div class="abs thumb" style="left:773px;background:linear-gradient(135deg,#7a1f25,#b0433f 50%,#4a1a1c)" role="img" aria-label="Collage of red curled hair colour results"></div>
</section>

<section class="prices">
  <h2 class="abs title" style="top:38px">Our Prices</h2>
  <div class="abs tab active" style="left:264px;width:152px">ADJUSTMENTS</div>
  <div class="abs tab" style="left:466px;width:140px">ARRANGEMENTS</div>
  <div class="abs tab" style="left:628px;width:140px">ATTATCHMENTS</div>
  <div class="abs tab" style="left:805px;width:140px">ENHANCEMENTS</div>

  <div class="abs price-card" style="left:155px;top:202px"><div class="row"><span class="name">Extension Removal</span><span class="cost">$100+</span><span class="dur">2 Hours</span></div><p>Lorem ipsum dolor sit amet, consectetur adipiscing elit. Proin osuere eros scelerisque maximus molestie. Class aptent taciti sociosqu litora torquent per conubia</p></div>
  <div class="abs price-card" style="left:609px;top:202px"><div class="row"><span class="name">Extension Removal</span><span class="cost">$100+</span><span class="dur">2 Hours</span></div><p>Lorem ipsum dolor sit amet, consectetur adipiscing elit. Proin osuere eros scelerisque maximus molestie. Class aptent taciti sociosqu litora torquent per conubia</p></div>
  <div class="abs price-card" style="left:155px;top:341px"><div class="row"><span class="name">Extension Removal</span><span class="cost">$100+</span><span class="dur">2 Hours</span></div><p>Lorem ipsum dolor sit amet, consectetur adipiscing elit. Proin osuere eros scelerisque maximus molestie. Class aptent taciti sociosqu litora torquent per conubia</p></div>
  <div class="abs price-card" style="left:609px;top:341px"><div class="row"><span class="name">Extension Removal</span><span class="cost">$100+</span><span class="dur">2 Hours</span></div><p>Lorem ipsum dolor sit amet, consectetur adipiscing elit. Proin osuere eros scelerisque maximus molestie. Class aptent taciti sociosqu litora torquent per conubia</p></div>

  <div class="abs btn book">Ready To Book?</div>
</section>

<section class="reviews">
  <h2 class="abs title" style="top:48px;font-size:26px">Customer Recommendations</h2>
  <svg class="abs" style="left:124px;top:234px" width="14" height="20" viewBox="0 0 14 20"><path d="M11 2 3 10l8 8" fill="none" stroke="#fff" stroke-width="2.5"/></svg>
  <svg class="abs" style="left:1060px;top:234px" width="14" height="20" viewBox="0 0 14 20"><path d="m3 2 8 8-8 8" fill="none" stroke="#fff" stroke-width="2.5"/></svg>
  <div class="abs face small" style="left:259px;top:244px" role="img" aria-label="Client portrait"></div>
  <div class="abs face small" style="left:418px;top:244px" role="img" aria-label="Client portrait"></div>
  <div class="abs face big" style="left:600px;top:236px" role="img" aria-label="Featured client portrait"></div>
  <svg class="abs" style="left:588px;top:324px" width="24" height="14" viewBox="0 0 24 14"><path d="M0 0h24L12 14z" fill="#d3d3d3"/></svg>
  <div class="abs face small" style="left:782px;top:244px" role="img" aria-label="Client portrait"></div>
  <div class="abs face small" style="left:941px;top:244px" role="img" aria-label="Client portrait"></div>
  <p class="abs quote">Lorem dolor sit amet consectetuer adipiscing elit Lorem ipsum dolor sit amet consectetuer<br>adipiscing elit Lorem ipsum dolor sit amet consectetuer adipiscing elit</p>
  <p class="abs cite">Marisa T. &nbsp;<span>Northline Studio</span></p>
  <div class="abs dots"><i></i><i></i><i></i><i></i></div>
</section>

<section class="map" role="img" aria-label="Street map showing the salon location in Dallas"></section>

<footer class="site-footer">
  <div class="abs foot-mark"></div>
  <div class="abs foot-brand">DANNOKE CURLS</div>
  <div class="abs portrait" role="img" aria-label="Black and white portrait of the stylist"></div>
  <div class="abs contact">
    <h4>DANNOKE CURLS</h4>
    Lumen Salon Suite<br>4120 Crescent Road, 9 Dallas, TX
    <div class="phone">214-555-0172</div>
    info@dannokecurls.com
  </div>
  <div class="abs rule"></div>
  <p class="abs copy">© 2016 Copyright Dannoke Curls. All Rights Reserved.</p>
  <div class="abs pay">Coinvex</div>
  <div class="abs social foot-social"><span></span><span></span></div>
</footer>

</body>
</html>
```